Business Card Design

We are a cutting edge natural health care provider who specializes in neuro behavioral conditions. We use brain mapping, neurofeedback, functional neurology and functional medicine to help people achieve their health goals.
We need a business card design for a new office. Would like to position ourselves as an upscale/concierge level treatment center that provides hope and results to people with chronic conditions. We would like the card to feature a brain, possibly a die cut shape. Design needs to communicate our tag line of "providing excellent care for difficult cases."
On back side of card:
By retraining abnormal brainwave patterns and eliminating metabolic problems, our programs often improve symptoms of:
ADD/ADHD
Addiction
Anxiety
Autism
Depression
Fibromyalgia
Insomnia
Memory Loss
Sensory/Motor Dysfunction

Target Market(s)

30-60 year olds with chronic conditions (Anxiety, depression,) or parents of children with chronic conditions (ADHD, autism, learning disorders, etc)

Industry/Entity Type

Health

Contact Information for Business Card

The Halvorsen Clinic
Dr. Colin Halvorsen, DC
4260 Orchard Pkwy. Suite 207
Maplewood, GA 30150
(555) 418-6623
Fax (555) 418-7044
www.TheHalvorsenClinic.example
www.DrColinHalvorsen.example

Requirements
Nice to have
• Picture of a brain that really pops on the page.

```html
<!DOCTYPE html>
<html lang="en">
<head>
<meta charset="utf-8">
<title>The Halvorsen Clinic — Business Card</title>
<link rel="stylesheet" href="https://fonts.googleapis.com/css2?family=Anton&family=Open+Sans:wght@400;600;700&display=swap">
<style>
  :root {
    --clinic-green: #2fbf24;
    --clinic-navy: #1d3a6e;
    --card-white: #fbfbfb;
    --text-gray: #2a3550;
    --backdrop: #e9e6e1;
    --art-pink: #d94b8a;
    --art-blue: #4a86d0;
    --art-orange: #f0a04c;
  }
  * { box-sizing: border-box; margin: 0; padding: 0; }
  html, body { width: 1200px; height: 880px; overflow: hidden; }
  body {
    background: var(--backdrop);
    font-family: "Open Sans", sans-serif;
    position: relative;
  }
  .card {
    position: absolute;
    width: 560px;
    height: 320px;
    box-shadow: 0 6px 18px rgba(0,0,0,0.18);
    overflow: hidden;
  }

  /* Back side */
  .card-back { left: 50px; top: 110px; background: var(--clinic-green); }
  .back-rail {
    position: absolute; left: 0; top: 0; bottom: 0; width: 84px;
    background: var(--clinic-navy);
    border-right: 4px solid #fff;
  }
  .rail-urls {
    position: absolute; left: 50%; top: 50%;
    transform: translate(-50%, -50%) rotate(-90deg);
    white-space: nowrap; color: #fff; font-size: 16px; line-height: 1.4;
  }
  .back-content {
    position: absolute; left: 84px; right: 0; top: 0; bottom: 0;
    padding: 30px 30px 0 30px; text-align: center;
  }
  .clinic-name-back { font-family: "Anton", sans-serif; font-weight: 400; color: #fff; font-size: 30px; line-height: 1.2; }
  .back-intro {
    color: var(--clinic-navy); font-size: 13.5px; line-height: 1.4;
    width: 330px; margin: 8px auto 0;
  }
  .symptom-columns { display: flex; gap: 40px; margin: 16px 0 0 20px; text-align: left; }
  .symptom-list { list-style: none; color: #fff; font-weight: 700; font-size: 15px; line-height: 1.45; }
  .symptom-list li::before { content: "• "; color: var(--clinic-navy); }
  .symptom-list .nowrap { white-space: nowrap; }

  /* Front side */
  .card-front { left: 590px; top: 450px; background: var(--card-white); }
  .clinic-name-front {
    position: absolute; left: 36px; top: 26px;
    font-family: "Anton", sans-serif; font-weight: 400; color: var(--clinic-green); font-size: 29px; line-height: 1.2;
  }
  .doctor-name { position: absolute; left: 36px; top: 96px; color: var(--clinic-navy); font-weight: 700; font-size: 17px; }
  .contact-block {
    position: absolute; left: 36px; top: 136px;
    color: var(--text-gray); font-size: 13.5px; line-height: 1.42; text-align: right; font-style: normal;
  }
  .contact-block .url { text-align: left; }
  .tagline {
    position: absolute; left: 330px; top: 60px; width: 200px;
    color: var(--clinic-green); font-size: 16px; line-height: 1.3; text-align: center;
  }
  .brain-art {
    position: absolute; left: 355px; top: 118px; width: 150px; height: 120px;
    border-radius: 10px;
    background: radial-gradient(circle at 35% 40%, var(--art-pink), var(--art-blue) 60%, var(--art-orange));
    opacity: 0.8;
  }
  .front-bands { position: absolute; left: 0; right: 0; bottom: 0; height: 14px; display: flex; }
  .front-bands span { height: 100%; }
  .band-navy-short { width: 28px; background: var(--clinic-navy); }
  .band-gap { width: 4px; background: #fff; }
  .band-green { width: 186px; background: var(--clinic-green); }
  .band-navy-long { flex: 1; background: var(--clinic-navy); }
</style>
</head>
<body>
  <section class="card card-back" aria-label="Card back">
    <div class="back-rail">
      <div class="rail-urls">www.TheHalvorsenClinic.example<br>www.DrColinHalvorsen.example</div>
    </div>
    <div class="back-content">
      <h1 class="clinic-name-back">The Halvorsen Clinic</h1>
      <p class="back-intro">By retraining abnormal brainwave patterns and eliminating metabolic problems our programs often improve symptoms of:</p>
      <div class="symptom-columns">
        <ul class="symptom-list">
          <li>ADD/ADHD</li>
          <li>Addiction</li>
          <li>Anxiety</li>
          <li>Autism</li>
          <li class="nowrap">Sensory/Motor Dysfunction</li>
        </ul>
        <ul class="symptom-list">
          <li>Depression</li>
          <li>Fibromyalgia</li>
          <li>Insomnia</li>
          <li>Memory Loss</li>
        </ul>
      </div>
    </div>
  </section>

  <section class="card card-front" aria-label="Card front">
    <h2 class="clinic-name-front">The Halvorsen Clinic</h2>
    <p class="doctor-name">Dr. Colin Halvorsen, DC</p>
    <address class="contact-block">
      4260 Orchard Pkwy., Suite 207<br>
      Maplewood, GA 30150<br>
      P: (555) 418-6623<br>
      F: (555) 418-7044
      <div class="url">www.TheHalvorsenClinic.example</div>
      <div class="url">www.DrColinHalvorsen.example</div>
    </address>
    <p class="tagline">providing excellent care for difficult cases</p>
    <div class="brain-art" role="img" aria-label="Colourful network-of-dots illustration of a brain"></div>
    <div class="front-bands">
      <span class="band-navy-short"></span><span class="band-gap"></span>
      <span class="band-green"></span><span class="band-gap"></span>
      <span class="band-navy-long"></span>
    </div>
  </section>
</body>
</html>
```